Maple Ridge business card design

Card needs to include the following text/items:
Company Logo
Tobin Marsh
Phone # - 555-318-7642
service@mapleridgelandscaping.example
Lawn & landscape maintenance services

```html
<!DOCTYPE html>
<html lang="en">
<head>
<meta charset="utf-8">
<title>Maple Ridge Landscaping – Business Card</title>
<link href="https://fonts.googleapis.com/css2?family=Montserrat:wght@400;500;700;800&display=swap" rel="stylesheet">
<style>
  :root {
    --bg: #25292b;
    --forest: #0f2e1c;
    --paper: #f4f4f3;
    --white: #ffffff;
    --bark: #8a4320;
    --ink: #1b2b22;
  }
  * { margin: 0; padding: 0; box-sizing: border-box; }
  html, body {
    width: 1200px; height: 898px; overflow: hidden;
    background: var(--bg);
    font-family: "Montserrat", Arial, sans-serif;
  }
  .sheet {
    width: 1200px; height: 898px;
    display: flex; flex-direction: column; align-items: center; justify-content: center;
    gap: 40px;
  }
  .card {
    position: relative;
    width: 700px; height: 400px;
    border-radius: 36px;
    overflow: hidden;
  }

  /* Shared brand block */
  .brand {
    position: absolute;
    display: flex; flex-direction: column; align-items: center;
  }
  .brand__mark {
    border-radius: 50%;
    background: linear-gradient(160deg, #5cc3ea 0%, #3f8a3a 55%, #1f5a2a 100%);
    border: 4px solid #8fb44a;
  }
  .brand__name {
    font-weight: 700; letter-spacing: 1px;
    white-space: nowrap; line-height: 1;
  }

  /* Front */
  .card--front { background: var(--forest); }
  .front__band {
    position: absolute; left: 0; right: 0; top: 188px; height: 157px;
    background: var(--paper);
  }
  .card--front .brand { left: 470px; top: 22px; width: 190px; }
  .card--front .brand__mark { width: 112px; height: 112px; }
  .card--front .brand__name { margin-top: 12px; font-size: 26px; color: var(--white); }

  .person {
    position: absolute; left: 44px; top: 218px;
    color: var(--ink);
  }
  .person__name { font-weight: 800; font-size: 34px; color: var(--forest); line-height: 1; }
  .person__role { font-weight: 400; font-size: 15px; margin-top: 6px; }
  .person__tagline {
    font-weight: 700; font-size: 12.5px; margin-top: 14px; line-height: 1.35;
  }
  .divider {
    position: absolute; left: 336px; top: 210px;
    width: 7px; height: 112px; background: var(--forest);
  }
  .contacts {
    position: absolute; left: 360px; top: 212px;
    list-style: none;
    font-size: 13px; font-weight: 400; color: var(--ink);
  }
  .contacts li { display: flex; align-items: center; gap: 12px; height: 36px; white-space: nowrap; }
  .contacts svg { width: 15px; height: 15px; fill: var(--forest); flex: none; }

  /* Back */
  .card--back { background: var(--paper); }
  .card--back .brand { left: 200px; top: 52px; width: 300px; }
  .card--back .brand__mark { width: 140px; height: 140px; }
  .card--back .brand__name { margin-top: 16px; font-size: 36px; color: var(--forest); }
  .back__band {
    position: absolute; left: 0; right: 0; top: 300px; height: 44px;
    background: var(--bark);
    display: flex; align-items: center; justify-content: center;
    color: var(--white); font-weight: 700; font-size: 19px; letter-spacing: 0.3px;
  }
</style>
</head>
<body>
<main class="sheet">

  <section class="card card--front" aria-label="Business card front">
    <div class="front__band"></div>
    <div class="brand">
      <div class="brand__mark" role="img" aria-label="Company emblem area: sky, trees and green hills"></div>
      <div class="brand__name">Maple Ridge</div>
    </div>

    <div class="person">
      <h1 class="person__name">Tobin Marsh</h1>
      <p class="person__role">Manager</p>
      <p class="person__tagline">Lawn &amp;<br>landscape maintenance services</p>
    </div>

    <div class="divider"></div>

    <ul class="contacts">
      <li>
        <svg viewBox="0 0 16 16" aria-hidden="true"><path d="M1 7.5 15 1 9.5 15 7.8 9.2Z"/></svg>
        service@mapleridgelandscaping.example
      </li>
      <li>
        <svg viewBox="0 0 16 16" aria-hidden="true"><path d="M2 5c0-2 2-3 6-3s6 1 6 3v1h-3V4.5H5V6H2Z"/><rect x="3" y="7" width="10" height="7" rx="1.5"/></svg>
        +1 555-318-7642
      </li>
      <li>
        <svg viewBox="0 0 16 16" aria-hidden="true"><circle cx="8" cy="8" r="7"/><path d="M1 8h14M8 1c3 3 3 11 0 14M8 1c-3 3-3 11 0 14" stroke="#f4f4f3" stroke-width="1.2" fill="none"/></svg>
        www.mapleridgelandscaping.example
      </li>
    </ul>
  </section>

  <section class="card card--back" aria-label="Business card back">
    <div class="brand">
      <div class="brand__mark" role="img" aria-label="Company emblem area: sky, trees and green hills"></div>
      <div class="brand__name">Maple Ridge</div>
    </div>
    <div class="back__band">Lawn &amp; landscape maintenance services</div>
  </section>

</main>
</body>
</html>
```